Dental office needs a newspaper ad to encourage new patients to join our practice

"October Teeth Whitening Special" Call today to schedule your next dental cleaning and exam and receive a free bleach kit. (small disclaimer at the bottom of the ad) Dr. Halvorsen and his staff follow the most up-to-date NHA infection control guidelines to protect our patients from CoVid-19 exposure. We offer a full spectrum of dental services including oral surgery, implants, root canals and cosmetic crowns and bridges. Our staff of licensed dental hygienists provide continued periodontal care for the healthiest teeth and gums. Visit our website. These are just some ideas you might be able to use. Also mention that most insurances are accepted. Emergencies and new patients welcome. As softer southern style motif like in our website can be used as a backdrop. The color scheme of the business logo and stationery is the same as the website.
Target Market(s)
All ages, local population 8,000 southern farming community. White Hispanic older population. Not oriented towards children.
Requirements
Must have
- Nice color. See our website at halvorsendentalcare.example for basic image of practice
Nice to have
- It will be a quarter to half page in a local newspaper, so it can be good sized with plenty of print an graphics

```html
<!DOCTYPE html>
<html lang="en">
<head>
<meta charset="utf-8">
<title>October Teeth Whitening Special – Halvorsen Dental Care</title>
<link rel="stylesheet" href="https://fonts.googleapis.com/css2?family=Montserrat:wght@400;500;600;700;800;900&display=swap">
<style>
  :root {
    --green: #74bf44;
    --cyan: #00b0d8;
    --navy: #14223a;
    --ink: #11213a;
    --hero-light: #e6e7f0;
    --hero-mid: #cfd1de;
    --skin: #ecc9c0;
    --lip: #d98f8f;
    --tooth: #fbf9f6;
    --guide: #8f9096;
    --white: #ffffff;
  }
  * { margin: 0; padding: 0; box-sizing: border-box; }
  html, body { width: 1200px; height: 800px; overflow: hidden; background: #ffffff; }
  body { font-family: "Montserrat", sans-serif; color: var(--ink); }

  .ad { position: relative; width: 1200px; height: 800px; overflow: hidden;
        background: linear-gradient(90deg, var(--hero-light) 0%, #dddeea 40%, var(--hero-mid) 60%); }

  .top-band { position: absolute; left: 0; top: 0; width: 1200px; height: 24px; background: var(--green); }

  .hero-photo { position: absolute; left: 540px; top: 24px; width: 660px; height: 620px;
    background:
      linear-gradient(90deg, rgba(207,209,222,1) 0%, rgba(207,209,222,0) 28%),
      linear-gradient(180deg,
        #f0d6cf 0%, var(--skin) 14%, #e2a9a3 24%,
        var(--tooth) 32%, #f3eeea 44%,
        var(--lip) 52%, #e8b2ad 60%,
        #f4f1ee 66%, #ebe8e6 76%,
        #b9b9bf 84%, var(--guide) 100%); }

  .month-pill { position: absolute; left: 97px; top: 71px; width: 315px; height: 51px; border-radius: 26px;
    background: var(--cyan); color: var(--white); font-weight: 900; font-size: 40px; letter-spacing: 9px;
    display: flex; align-items: center; justify-content: center; padding-left: 8px; }

  .headline { position: absolute; left: 66px; top: 116px; font-weight: 800; color: var(--ink); line-height: 1; letter-spacing: -3px; }
  .headline .line-teeth { display: block; font-size: 104px; }
  .headline .line-whitening { display: block; font-size: 78px; margin-top: -8px; margin-left: -6px; letter-spacing: -2.5px; }
  .tooth-icon { position: absolute; left: 357px; top: 131px; width: 98px; height: 92px; }

  .special { position: absolute; left: 134px; top: 282px; color: var(--green); font-weight: 900;
    font-size: 40px; letter-spacing: 9px; }

  .call-pill { position: absolute; left: 99px; top: 337px; width: 188px; height: 31px; border-radius: 16px;
    background: var(--green); color: var(--white); font-weight: 800; font-size: 20px; letter-spacing: 2px;
    display: flex; align-items: center; justify-content: center; }

  .phone { position: absolute; left: 52px; top: 369px; display: flex; align-items: center; gap: 4px;
    color: var(--cyan); font-weight: 800; font-size: 41px; letter-spacing: -1px; }
  .phone svg { width: 22px; height: 32px; }

  .offer { position: absolute; left: 58px; top: 414px; width: 300px; text-align: center; color: var(--ink); line-height: 13px; }
  .offer .offer-line { display: block; font-size: 11px; font-weight: 500; text-transform: uppercase; }
  .offer strong { font-weight: 700; }
  .offer .offer-gift { display: block; font-size: 20px; font-weight: 800; line-height: 24px; margin-top: 2px; }

  .kit-photo { position: absolute; left: 342px; top: 356px; width: 156px; height: 124px; border-radius: 12px;
    background: linear-gradient(160deg, #2a86c9 0%, #1d6fb4 45%, #dfe7f1 72%, #f6f9fc 100%); }

  .services-band { position: absolute; left: 0; top: 503px; width: 740px; height: 141px; }
  .thumb { position: absolute; top: 520px; width: 141px; height: 109px; }
  .thumb-exam { left: 0; background: linear-gradient(160deg, #e9b9ae 0%, #f7f3f1 45%, #d8c3bc 75%, #7fb1e3 100%); }
  .thumb-aligner { left: 152px; background: linear-gradient(90deg, #6fc0dc 0%, #e8c3ad 40%, #f1d6c7 65%, #f7f1ec 100%); }
  .thumb-smile { left: 304px; background: linear-gradient(180deg, #eec9bd 0%, #d99791 35%, #fbf8f5 55%, #e9bcb0 100%); }

  .services-text { position: absolute; left: 464px; top: 527px; width: 225px; font-size: 11.3px; line-height: 14px;
    color: var(--ink); font-weight: 400; }
  .services-text strong { font-weight: 700; }

  .footer { position: absolute; left: 0; top: 643px; width: 1200px; height: 157px; background: var(--navy); }
  .doctor-photo { position: absolute; left: 0; top: 613px; width: 217px; height: 187px; border-radius: 0 90px 0 0;
    background: linear-gradient(180deg, #d9c2b4 0%, #c9cfd9 40%, #f2f4f7 65%, #dfe5ee 100%); }

  .notes { position: absolute; left: 236px; top: 678px; list-style: none; color: var(--white); }
  .notes li { position: relative; padding-left: 18px; }
  .notes li::before { content: ""; position: absolute; left: 0; width: 8px; height: 8px; border-radius: 50%; background: var(--green); }
  .notes .note-small { font-size: 11.3px; line-height: 14.5px; width: 335px; margin-bottom: 11px; }
  .notes .note-small::before { top: 3px; }
  .notes .note-large { font-size: 15.5px; line-height: 23px; letter-spacing: 0.3px; }
  .notes .note-large::before { top: 8px; }

  .divider { position: absolute; left: 614px; top: 662px; height: 120px; border-left: 3px dotted var(--green); }

  .practice-mark { position: absolute; left: 664px; top: 681px; width: 44px; height: 44px; border-radius: 50%; background: #9aa0aa; }
  .practice-info { position: absolute; left: 732px; top: 670px; width: 440px; text-align: center; }
  .practice-name { color: var(--white); font-weight: 600; font-size: 35px; line-height: 44px; white-space: nowrap; }
  .practice-address { margin-top: 12px; color: var(--white); font-size: 14.5px; font-weight: 500; line-height: 20px;
    display: flex; align-items: center; justify-content: center; gap: 4px; white-space: nowrap; }
  .practice-web { margin-top: 2px; color: var(--green); font-size: 19px; font-weight: 700; line-height: 26px;
    display: flex; align-items: center; justify-content: center; gap: 6px; white-space: nowrap; }
</style>
</head>
<body>
<main class="ad">
  <div class="top-band"></div>

  <div class="hero-photo" role="img" aria-label="Close-up of a bright white smile beside a tooth shade guide"></div>

  <div class="month-pill">OCTOBER</div>
  <h1 class="headline">
    <span class="line-teeth">Teeth</span>
    <span class="line-whitening">Whitening</span>
  </h1>
  <svg class="tooth-icon" viewBox="0 0 100 95" aria-hidden="true">
    <path d="M28 6 C12 6 4 20 6 36 C8 52 14 60 18 74 C21 86 28 92 33 82 C38 70 40 56 50 56 C60 56 62 70 67 82 C72 92 79 86 82 74 C86 60 92 52 94 36 C96 20 88 6 72 6 C62 6 58 12 50 12 C42 12 38 6 28 6 Z"
          fill="none" stroke="#00b0d8" stroke-width="7" stroke-linejoin="round"/>
  </svg>
  <div class="special">SPECIAL</div>

  <div class="call-pill">CALL TODAY</div>
  <div class="phone">
    <svg viewBox="0 0 22 32" aria-hidden="true">
      <path d="M7 2 L11 2 L12 9 L9 11 C9 17 11 21 14 23 L17 21 L21 27 L18 30 C9 30 3 21 3 12 C3 7 5 3 7 2 Z" fill="#00b0d8"/>
    </svg>
    <span>555 014 0219</span>
  </div>
  <p class="offer">
    <span class="offer-line">Schedule your next <strong>dental cleaning</strong><br>and <strong>exam</strong> and receive a</span>
    <strong class="offer-gift">FREE BLEACH KIT</strong>
  </p>
  <div class="kit-photo" role="img" aria-label="Home whitening kit with case, trays and gel syringes"></div>

  <svg class="services-band" viewBox="0 0 740 141" aria-hidden="true">
    <polygon points="0,0 680,0 737,141 0,141" fill="#74bf44"/>
  </svg>
  <div class="thumb thumb-exam" role="img" aria-label="Dental exam with a mirror"></div>
  <div class="thumb thumb-aligner" role="img" aria-label="Smiling woman holding a clear aligner"></div>
  <div class="thumb thumb-smile" role="img" aria-label="Person fitting a clear aligner on the teeth"></div>
  <p class="services-text">We offer a full spectrum of dental services including <strong>ORAL SURGERY, IMPLANTS, ROOT CANALS, COSMETIC CROWNS</strong> and <strong>BRIDGES.</strong> Our staff of licensed dental hygienists provide continued periodontal care for the healthiest teeth and gums.</p>

  <footer class="footer"></footer>
  <div class="doctor-photo" role="img" aria-label="Portrait of the dentist in a white coat and tie"></div>

  <ul class="notes">
    <li class="note-small">Dr. Halvorsen and his staff follow the most up-to-date NHA infection control guidelines to protect our patients from CoVid-19 exposure.</li>
    <li class="note-large">Most insurances are accepted.</li>
    <li class="note-large">Emergencies and new patients welcome.</li>
  </ul>

  <div class="divider"></div>

  <div class="practice-mark"></div>
  <div class="practice-info">
    <div class="practice-name">Erik J. Halvorsen, DMD</div>
    <div class="practice-address">
      <svg width="12" height="16" viewBox="0 0 12 16" aria-hidden="true">
        <path d="M6 0 C2.7 0 0 2.6 0 6 C0 10 6 16 6 16 C6 16 12 10 12 6 C12 2.6 9.3 0 6 0 Z" fill="#74bf44"/>
        <circle cx="6" cy="6" r="2.3" fill="#14223a"/>
      </svg>
      48 Magnolia Ave Cypress Bend, FL 34012
    </div>
    <div class="practice-web">
      <svg width="18" height="18" viewBox="0 0 18 18" aria-hidden="true">
        <circle cx="8" cy="8" r="7" fill="none" stroke="#74bf44" stroke-width="1.6"/>
        <path d="M1 8 H15 M8 1 C4 5 4 11 8 15 M8 1 C12 5 12 11 8 15" fill="none" stroke="#74bf44" stroke-width="1.3"/>
      </svg>
      www.halvorsendentalcare.example
    </div>
  </div>
</main>
</body>
</html>
```